Design a Mobile App for Landscape Businesses

This project is to design the first three screens for a mobile app for Landscape and Lawncare businesses. This app will serve as a directory for homeowners to locate landscape and lawn care businesses and for landscape businesses and contractors to run their business. See the attached PDF for more information and example
Here is the link to the description https://lnkshrt.example/q7Tz3K

Target Market(s)

Landscape and lawn care business, gardeners, home owners

Industry/Entity Type

Landscape Gardening

Logo Text

Velmarigo

Colors

Designer to choose colors to be used in the design.

```html
<!DOCTYPE html>
<html lang="en">
<head>
<meta charset="UTF-8">
<title>Velmarigo – Register Your Business</title>
<link rel="stylesheet" href="https://fonts.googleapis.com/css2?family=Montserrat:wght@400;500;600;700&display=swap">
<style>
  :root {
    --ink: #232a36;
    --ink-soft: #2e3747;
    --page: #eef2f5;
    --white: #ffffff;
    --field-border: #e1e6ea;
    --green: #3aa535;
    --blue-a: #2a63b1;
    --blue-b: #2f82c2;
    --aqua-a: #26a6e1;
    --aqua-b: #1fcbd9;
  }
  * { box-sizing: border-box; margin: 0; padding: 0; }
  html, body { width: 675px; height: 1200px; overflow: hidden; }
  body {
    position: relative;
    background: var(--page);
    font-family: "Montserrat", sans-serif;
    color: var(--ink);
  }
  .status-bar {
    position: absolute; top: 0; left: 0; width: 675px; height: 36px;
    background: var(--white);
    display: flex; align-items: center; justify-content: flex-end;
    gap: 8px; padding-right: 18px;
    font-size: 21px; font-weight: 500; color: #333;
  }
  .status-bar svg { display: block; }
  .app-header {
    position: absolute; top: 36px; left: 0; width: 675px; height: 90px;
    background: var(--white);
  }
  .app-header__title {
    position: absolute; left: 20px; top: 26px;
    font-size: 27px; font-weight: 700; line-height: 34px; color: var(--ink);
  }
  .app-header__close { position: absolute; right: 20px; top: 24px; }
  .progress-bar {
    position: absolute; top: 126px; left: 0; width: 675px; height: 8px;
    background: var(--green);
  }
  .section-title {
    position: absolute; left: 22px; top: 188px;
    font-size: 35px; font-weight: 500; line-height: 44px; color: var(--ink-soft);
  }
  .field-label {
    position: absolute; left: 20px;
    font-size: 19px; font-weight: 600; line-height: 22px;
    text-transform: uppercase; letter-spacing: 0.3px; color: var(--ink);
  }
  .field {
    position: absolute; left: 16px; width: 641px; height: 81px;
    background: var(--white);
    border: 1.5px solid var(--field-border); border-radius: 3px;
    padding-left: 22px;
    display: flex; align-items: center;
    font-size: 23px; font-weight: 400; color: var(--ink);
  }
  .social-button, .register-button {
    position: absolute; left: 20px; width: 639px; height: 81px;
    border-radius: 5px;
    display: flex; align-items: center; justify-content: center; gap: 14px;
    font-size: 23px; font-weight: 700; color: var(--white);
  }
  .social-button--socialbook { top: 770px; background: linear-gradient(90deg, var(--blue-a), var(--blue-b)); }
  .social-button--chirper { top: 869px; background: linear-gradient(90deg, var(--aqua-a), var(--aqua-b)); }
  .social-button__mark { width: 26px; height: 26px; background: var(--white); border-radius: 3px; opacity: 0.95; }
  .social-button--chirper .social-button__mark { border-radius: 50%; }
  .register-button { top: 1096px; background: var(--green); }
  .bottom-edge { position: absolute; left: 0; top: 1194px; width: 675px; height: 6px; background: #d9dfe3; }
</style>
</head>
<body>
  <div class="status-bar">
    <svg width="20" height="20" viewBox="0 0 20 20" aria-hidden="true"><circle cx="10" cy="11" r="7" fill="none" stroke="#333" stroke-width="2"/><path d="M10 7v4l3 2" stroke="#333" stroke-width="2" fill="none"/></svg>
    <svg width="22" height="18" viewBox="0 0 22 18" aria-hidden="true"><path d="M1 5a15 15 0 0 1 20 0L11 17z" fill="#333"/></svg>
    <svg width="20" height="18" viewBox="0 0 20 18" aria-hidden="true"><path d="M19 1v16H1z" fill="#333"/></svg>
    <svg width="12" height="20" viewBox="0 0 12 20" aria-hidden="true"><rect x="1" y="3" width="10" height="16" rx="1" fill="none" stroke="#333" stroke-width="2"/><rect x="4" y="0" width="4" height="3" fill="#333"/><rect x="3" y="12" width="6" height="5" fill="#333"/></svg>
    <span>16:54</span>
  </div>

  <header class="app-header">
    <h1 class="app-header__title">Register Your Business</h1>
    <svg class="app-header__close" width="36" height="36" viewBox="0 0 36 36" aria-label="Close"><path d="M4 4l28 28M32 4L4 32" stroke="#232a36" stroke-width="3.5" stroke-linecap="round"/></svg>
  </header>
  <div class="progress-bar"></div>

  <h2 class="section-title">Contact Details (1/2)</h2>

  <label class="field-label" style="top:282px">Your Website URL</label>
  <div class="field" style="top:317px">www.velmarigo.com</div>

  <label class="field-label" style="top:424px">Your Phone Number</label>
  <div class="field" style="top:457px">01632 555 014</div>

  <label class="field-label" style="top:564px">City</label>
  <div class="field" style="top:598px">New York</div>

  <label class="field-label" style="top:730px">Social Media</label>
  <div class="social-button social-button--socialbook"><span class="social-button__mark"></span>Connect Socialbook</div>
  <div class="social-button social-button--chirper"><span class="social-button__mark"></span>Connect Chirper</div>

  <div class="register-button">
    <svg width="28" height="28" viewBox="0 0 28 28" aria-hidden="true"><circle cx="14" cy="14" r="12" fill="none" stroke="#fff" stroke-width="2.5"/><path d="M8.5 14.5l4 4 7-8" fill="none" stroke="#fff" stroke-width="2.5" stroke-linecap="round" stroke-linejoin="round"/></svg>
    Register
  </div>
  <div class="bottom-edge"></div>
</body>
</html>
```